Norwegian Mobile Home/Cabin Producer Needs Brochure Design

We make and deliver our own brand of mobile homes especially made for Norway and it's weather conditions. We differ from other brands in building quality in regards to a much more solid construction, insulation and choices. We work with our customer from the beginning and build them after their demands and wishes.
We need a brochure that holds us out as top of the line. We deliver mobile homes of all kinds and sizes. Both to the private and professional sector.
For the professional sector, mainly camping sites we want to show, lodges-, sanitary- and kitchen wagoons etc.
So we need a brochure of 14-20 pages in A4 where the double pages can be printed in A3 format.
We have logo (provided). But we need cover as well as back suggestions.
It should start with pages where we can teel who we are and stand for.Piicture(s) and space for some editable text (which we can write in norwegian). The text part can have a transparent background......or not. Give us your best shot. Also a smaller part in the private sector that shows winter time.
We want other pages for the private sector that shows what we deliver and the possibilities of choices.
Pages for the the professional sector.
Pages that show our production. How we transport. And the split construction. Only pictures from this portfolio here. (see fotoskap portfolios)
Take a look at provided pictures and our website www.solvikhytta.no for inspiration.
Here's a FotoSkap link to Pictures to choose from. http://bildelagr.example/K4TQ9P
(Hope it Works, let me know if not)
Our company name in small letters "fjordgrønn hyttebygg" means directly translated "fjordgreen cabin builds".
Looking forward to your suggestions.
Target Market(s)
Private market for vacation mobile homes. Camping sites and similar
Industry/Entity Type
Insulation
Requirements
Must have
- Our logo on the front page. Simple but inviting and professional
Logo and address on the back.

```html
<!DOCTYPE html>
<html lang="no">
<head>
<meta charset="utf-8">
<title>fjordgrønn hyttebygg as – omslag</title>
<link rel="stylesheet" href="https://fonts.googleapis.com/css2?family=Cabin:wght@400;700&display=swap">
<style>
  :root {
    --back-top: #7cc7f3;
    --back-mid: #3fb0ea;
    --back-bottom: #0a95da;
    --ring: #1b8fd5;
    --disc: #8fd5f6;
    --heading-blue: #1a70c0;
    --ink: #111820;
    --white: #ffffff;
    --sky-light: #eef7fc;
    --sky-mid: #b9dcf2;
    --sky-deep: #6fb4e3;
    --leaf-green: rgba(70, 170, 120, 0.75);
    --leaf-teal: rgba(60, 150, 175, 0.55);
    --shell-cream: rgba(246, 236, 196, 0.95);
    --shell-gold: rgba(226, 204, 130, 0.7);
    --sand-blue: rgba(90, 150, 215, 0.6);
    --logo-ink: #66708a;
    --font-text: "Cabin", "Gill Sans", Arial, sans-serif;
  }
  * { margin: 0; padding: 0; box-sizing: border-box; }
  html, body {
    width: 1200px; height: 849px; overflow: hidden; background: var(--white);
  }
  .spread {
    position: relative; display: flex; width: 1200px; height: 849px;
    font-family: var(--font-text);
  }
  .back-cover {
    position: relative; width: 600px; height: 849px;
    background: linear-gradient(180deg, var(--back-top) 0%, var(--back-mid) 45%, var(--back-bottom) 100%);
  }
  .contact-disc {
    position: absolute; left: 189px; top: 291px; width: 222px; height: 222px;
    border-radius: 50%; background: var(--disc);
    border: 8px solid var(--ring);
    display: flex; flex-direction: column; align-items: center; justify-content: center;
    text-align: center; color: var(--ink); font-size: 13px; line-height: 23px;
    font-style: normal; padding-top: 2px;
  }
  .contact-heading {
    color: var(--heading-blue); font-weight: 700; font-size: 15px; margin-bottom: 1px;
  }
  .web-address {
    position: absolute; left: 0; width: 600px; top: 537px;
    text-align: center; color: var(--white); font-size: 16px; letter-spacing: 0.2px;
  }
  .fold { width: 1px; height: 849px; background: var(--white); }
  .front-cover {
    position: relative; width: 599px; height: 849px; overflow: hidden;
  }
  .front-photo {
    position: absolute; inset: 0;
    background:
      radial-gradient(ellipse 230px 170px at 88% 14%, var(--leaf-green), transparent 75%),
      radial-gradient(ellipse 300px 120px at 62% 20%, var(--leaf-teal), transparent 80%),
      radial-gradient(ellipse 150px 230px at 86% 62%, var(--shell-cream), transparent 80%),
      radial-gradient(ellipse 90px 120px at 94% 66%, var(--shell-gold), transparent 85%),
      radial-gradient(ellipse 90px 70px at 50% 76%, rgba(230, 225, 160, 0.7), transparent 85%),
      radial-gradient(ellipse 320px 200px at 25% 78%, var(--sand-blue), transparent 80%),
      radial-gradient(ellipse 280px 260px at 20% 25%, var(--sky-light), transparent 80%),
      linear-gradient(180deg, var(--sky-mid) 0%, var(--sky-light) 42%, #a8d2ef 60%, var(--sky-deep) 100%);
  }
  .front-logo {
    position: absolute; left: 72px; top: 404px;
    font-size: 40px; font-weight: 400; color: var(--logo-ink);
    letter-spacing: 2.6px; white-space: nowrap; line-height: 1.2;
  }
</style>
</head>
<body>
  <main class="spread">
    <section class="back-cover">
      <address class="contact-disc">
        <span class="contact-heading">Kontaktinfo</span>
        <span>47 31 08 31</span>
        <span>fjordgrønn hyttebygg AS</span>
        <span>Postboks 14</span>
        <span>4712 Solvikstrand</span>
      </address>
      <p class="web-address">www.solvikhytta.no</p>
    </section>
    <div class="fold"></div>
    <section class="front-cover">
      <div class="front-photo" role="img" aria-label="Fotografi: lys himmel med skyer, grønt palmeblad øverst til høyre, et kremhvitt skjell og en krystallstjerne i glitrende blå sand"></div>
      <h1 class="front-logo">fjordgrønn hyttebygg as</h1>
    </section>
  </main>
</body>
</html>
```